Business Card Design

I need a design/ business card for a new company that caters for Event Hire (decorations and linen only) I am dabbling in rustic/ vintage designs for weddings and would like an elegant look to the cards. Something that will catch peoples eyes amongst the rest of the competitions cards and stand out to all fields, corporate/ weddings and general functions.

I am unsure of colours or pictures i would like so i am open to anything but possibly stick away from photos as i they are not more work of art on the card?
Updates

Target Market(s)

weddings and corporate events

Industry/Entity Type

Business

Contact Information for Business Card

Marlowe Weddings & Event Hire

Servicing the Gladstone Region for Weddings, Corporate & Private Functions

marloweweddings@postvale.net
Phone: 0427 814 253

Requirements
Must have
• The writing "Marlowe Weddings & Event Hire" please
Nice to have
• Something that really stands out as a must have at your event
Should not have
• Pictures that are not of my work

```html
<!DOCTYPE html>
<html lang="en">
<head>
<meta charset="utf-8">
<title>Marlowe Weddings &amp; Event Hire — Business Card</title>
<link rel="stylesheet" href="https://fonts.googleapis.com/css2?family=Comfortaa:wght@400;600&display=swap">
<style>
  :root {
    --page-bg: #e9e6e3;
    --card-white: #ffffff;
    --brand-teal: #13a582;
    --brand-teal-dark: #0f7f66;
    --card-black: #0b0b0b;
    --pattern-grey: #2a2a2a;
    --text-white: #ffffff;
  }
  * { box-sizing: border-box; margin: 0; padding: 0; }
  html, body {
    width: 1200px;
    height: 800px;
    overflow: hidden;
    background: var(--page-bg);
    font-family: "Comfortaa", sans-serif;
  }
  .business-card {
    position: absolute;
    left: 150px;
    top: 125px;
    width: 900px;
    height: 550px;
    background: var(--card-white);
    box-shadow: 0 10px 30px rgba(0,0,0,0.18);
    overflow: hidden;
  }
  .card-header {
    position: absolute;
    left: 0; top: 0;
    width: 100%;
    height: 300px;
    display: flex;
    align-items: center;
    justify-content: center;
  }
  .brand-name {
    color: var(--brand-teal-dark);
    font-weight: 600;
    font-size: 60px;
    line-height: 1.15;
    text-align: center;
    letter-spacing: 1px;
  }
  .brand-name span { display: block; }
  .tagline-band {
    position: absolute;
    left: 0; top: 300px;
    width: 100%;
    height: 40px;
    background: var(--brand-teal);
    color: var(--text-white);
    font-size: 19px;
    font-weight: 400;
    display: flex;
    align-items: center;
    justify-content: center;
    white-space: nowrap;
  }
  .contact-panel {
    position: absolute;
    left: 0; top: 340px;
    width: 100%;
    height: 210px;
    background: var(--card-black);
  }
  .damask-fill {
    position: absolute;
    inset: 0;
    background: radial-gradient(ellipse at 60% 40%, var(--pattern-grey) 0%, var(--card-black) 75%);
  }
  .contact-details {
    position: absolute;
    right: 70px;
    top: 40px;
    text-align: right;
  }
  .contact-phone {
    color: var(--brand-teal);
    font-size: 42px;
    font-weight: 600;
    letter-spacing: 1px;
  }
  .contact-email {
    margin-top: 22px;
    color: var(--text-white);
    font-size: 31px;
    font-weight: 400;
  }
</style>
</head>
<body>
  <main class="business-card">
    <header class="card-header">
      <h1 class="brand-name"><span>Marlowe Weddings</span><span>&amp; Event Hire</span></h1>
    </header>
    <p class="tagline-band">Servicing the Gladstone Region for Weddings, Corporate &amp; Private Functions</p>
    <section class="contact-panel">
      <div class="damask-fill" role="img" aria-label="Dark grey damask flourish pattern on black"></div>
      <div class="contact-details">
        <p class="contact-phone">0427 814 253</p>
        <p class="contact-email">marloweweddings@postvale.net</p>
      </div>
    </section>
  </main>
</body>
</html>
```